Geschäftspapiere für mobile Cocktailbar
Zielgruppe
Wir sind eine mobile Cocktailbar ! Wir arbeiten vielen Veranstaltungen / Festivals.
Ein sehr wichtiges Geschäftssegment sind Firmenveranstaltungen jeglicher Größe.
Hier stehen wir für sehr hohe Qualität an Service und an den Drinks.
Wir arbeiten stets mit Markenprodukten, professionellen Barkeepern und sehr hochwertigen Equipment
Unsere Website ist www.korbinel-bar.de
Aufgabenstellung
Es soll schlicht aber hochwertig sein
vielleicht eine Layout im Hintergrund
Drinks, Flüssigkeit, Bartending etc
Gerne auch das Logo eingebaut

```html
<!DOCTYPE html>
<html lang="de">
<head>
<meta charset="utf-8">
<title>Korbinel – Geschäftspapiere</title>
<link rel="stylesheet" href="https://fonts.googleapis.com/css2?family=Montserrat:ital,wght@0,300;0,400;0,600;0,800;1,400;1,800&display=swap">
<style>
  :root {
    --backdrop: #d6d6d6;
    --paper: #ffffff;
    --ink: #0a0a0a;
    --ink-soft: #2b2b2b;
    --faint: #ececec;
    --photo-dark: #05070d;
    --photo-glow: #7a1b24;
  }
  * { margin: 0; padding: 0; box-sizing: border-box; }
  html, body { width: 1200px; height: 864px; overflow: hidden; }
  body {
    position: relative;
    background: var(--backdrop);
    font-family: "Montserrat", sans-serif;
    color: var(--ink);
  }
  .sheet {
    position: absolute;
    background: var(--paper);
    box-shadow: 3px 4px 6px rgba(0,0,0,0.25);
    overflow: hidden;
  }
  .sheet--letter { left: 17px; top: 15px; width: 578px; height: 816px; }
  .sheet--follow { left: 610px; top: 24px; width: 577px; height: 816px; }

  .contact-list { position: absolute; left: 21px; top: 19px; list-style: none; }
  .contact-list li {
    display: flex; align-items: center;
    height: 22.2px;
    font-size: 9px; font-weight: 400;
  }
  .contact-list svg { width: 14px; height: 14px; margin-right: 18px; flex: none; }

  .masthead {
    position: absolute; left: 229px; top: 0; width: 349px; height: 95px;
    background: var(--ink);
  }
  .brand-box {
    position: absolute; left: 56px; top: 24px; width: 239px; height: 28px;
    background: var(--paper);
    display: flex; align-items: center; justify-content: center;
    font-size: 18px; font-weight: 800; letter-spacing: 5px; color: var(--ink);
  }
  .brand-url {
    position: absolute; left: 0; width: 100%; top: 57px;
    text-align: center; color: var(--paper);
    font-size: 6.5px; font-weight: 600; letter-spacing: 2px;
  }

  .letter-title {
    position: absolute; left: 230px; width: 318px; top: 135px;
    text-align: center;
    font-size: 13.5px; font-weight: 800; font-style: italic; letter-spacing: 2.6px;
  }
  .intro {
    position: absolute; left: 247px; width: 286px; top: 184px;
    text-align: center;
    font-size: 12.3px; font-style: italic; font-weight: 400; line-height: 15.1px;
    color: var(--ink-soft);
  }
  .photo {
    position: absolute; left: 0; top: 160px; width: 221px; height: 271px;
    background: radial-gradient(circle at 32% 52%, var(--photo-glow) 0%, #2a0c12 22%, var(--photo-dark) 48%);
  }
  .body-text {
    position: absolute; left: 24px; width: 515px; top: 496px;
    text-align: center;
    font-size: 11.3px; font-weight: 300; line-height: 14px;
    color: var(--ink-soft);
  }
  .bar-motif {
    position: absolute; width: 162px; height: 120px;
    background: linear-gradient(180deg, var(--faint), #f4f4f4);
    border-radius: 8px;
  }
  .sheet--letter .bar-motif { left: 208px; top: 631px; }
  .sheet--follow .bar-motif { left: 207px; top: 631px; }
  .signature {
    position: absolute; left: 425px; top: 644px; width: 114px; height: 87px;
    background: linear-gradient(90deg, #f7f7f7, #fbfbfb);
  }
  .rule { position: absolute; height: 2px; background: var(--ink); }
  .sheet--letter .rule { left: 42px; top: 756px; width: 494px; }
  .sheet--follow .rule { left: 42px; top: 756px; width: 494px; }
  .bank {
    position: absolute; left: 0; width: 100%; top: 767px;
    text-align: center; font-size: 8.6px; font-weight: 300; line-height: 15px;
  }
</style>
</head>
<body>

<section class="sheet sheet--letter">
  <ul class="contact-list">
    <li><svg viewBox="0 0 14 14"><circle cx="7" cy="7" r="7" fill="#0a0a0a"/><rect x="4.3" y="3.5" width="5.4" height="7" rx="1" fill="none" stroke="#fff" stroke-width="1.2"/></svg>Mobile Cocktailbar</li>
    <li><svg viewBox="0 0 14 14"><circle cx="7" cy="7" r="7" fill="#0a0a0a"/><path d="M4.5 3.8h2l.6 2-1 .8a5 5 0 0 0 2.3 2.3l.8-1 2 .6v2a1 1 0 0 1-1 1A6.6 6.6 0 0 1 3.5 4.8a1 1 0 0 1 1-1z" fill="#fff"/></svg>Phone</li>
    <li><svg viewBox="0 0 14 14"><circle cx="7" cy="7" r="7" fill="#0a0a0a"/><path d="M7 3a2.6 2.6 0 0 1 2.6 2.6C9.6 7.6 7 10.8 7 10.8S4.4 7.6 4.4 5.6A2.6 2.6 0 0 1 7 3z" fill="#fff"/><circle cx="7" cy="5.6" r="1" fill="#0a0a0a"/></svg>Location</li>
    <li><svg viewBox="0 0 14 14"><circle cx="7" cy="7" r="7" fill="#0a0a0a"/><path d="M3.5 6.8 10.5 3.5 7.2 10.5 6.4 7.6z" fill="#fff"/></svg>Address</li>
    <li><svg viewBox="0 0 14 14"><circle cx="7" cy="7" r="7" fill="#0a0a0a"/><circle cx="7" cy="7" r="4" fill="none" stroke="#fff" stroke-width="1.2"/><path d="M5 7.2 6.5 8.6 9.2 5.6" fill="none" stroke="#fff" stroke-width="1.2"/></svg>Website</li>
    <li><svg viewBox="0 0 14 14"><circle cx="7" cy="7" r="7" fill="#0a0a0a"/><rect x="3.5" y="4.5" width="7" height="5" rx=".8" fill="#fff"/><path d="M3.7 4.9 7 7.4l3.3-2.5" fill="none" stroke="#0a0a0a" stroke-width=".9"/></svg>Mail</li>
  </ul>

  <header class="masthead">
    <div class="brand-box">KORBINEL</div>
    <p class="brand-url">www.korbinel-crew.com</p>
  </header>

  <h1 class="letter-title">MOBILE COCKTAILBAR</h1>

  <p class="intro">Lorem ipsum dolor sit amet, consectetur adipiscing elit. Proin pretium neque at nibh ultricies, vel pretium risus volutpat. Fusce rhoncus, elit eu facilisis ultricies, velit leo pharetra sem, quis dignissim sapien lorem nec dui. Praesent dignissim tortor ante, quis venenatis ex tempus sed. Nulla turpis mauris, mollis non felis eu, egestas lobortis lectus. Nulla aliquet felis eget ullamcorper gravida. Nullam risus ipsum, sagittis vitae maximus quis, accumsan vel dolor. Curabitur metus quam, semper id semper at, bibendum eget diam. Curabitur vitae luctus neque. Vestibulum rhoncus ac nisl vitae porttitor. Morbi fringilla varius mi at imperdiet. Vestibulum aliquet, justo sed commodo ultrices, nulla libero elementum urna, sit amet porta felis dolor eu purus.</p>

  <div class="photo" role="img" aria-label="Foto eines roten Longdrinks mit Strohhalm und Minze auf einer Schieferplatte vor schwarzem Hintergrund"></div>

  <p class="body-text">Lorem ipsum dolor sit amet, consectetur adipiscing elit. Proin pretium neque at nibh ultricies, vel pretium risus volutpat. Fusce rhoncus, elit eu facilisis ultricies, velit leo pharetra sem, quis dignissim sapien lorem nec dui. Praesent dignissim tortor ante, quis venenatis ex tempus sed. Nulla turpis mauris, mollis non felis eu, egestas lobortis lectus. Nulla aliquet felis eget ullamcorper gravida. Nullam risus ipsum, sagittis vitae maximus quis, accumsan vel dolor. Curabitur metus quam, semper id semper at, bibendum eget diam. Curabitur vitae luctus neque. Vestibulum rhoncus ac nisl vitae porttitor. Morbi fringilla varius mi at imperdiet. Vestibulum aliquet, justo sed commodo ultrices, nulla libero elementum urna, sit amet porta felis dolor eu purus.</p>

  <div class="bar-motif" role="img" aria-label="Blasse Strichzeichnung von Cocktailgläsern und Shaker als Hintergrundmotiv"></div>
  <div class="signature" role="img" aria-label="Handschriftliche Unterschrift"></div>

  <div class="rule"></div>
  <p class="bank">Bank Details : 00-555554-56514511<br>Name of Bank</p>
</section>

<section class="sheet sheet--follow">
  <div class="bar-motif" role="img" aria-label="Blasse Strichzeichnung von Cocktailgläsern und Shaker als Hintergrundmotiv"></div>
  <div class="rule"></div>
</section>

</body>
</html>
```